GRA Stationary
GRA, Garnet Resale Advisors
Professional
Dominic T. Harlow
P.O. box 382
Fernbrook Hill, PA 19507
dtharlow@graadvllc.com
graadvllc.com
I'm open to all ideas. GRA specializes in estate or antique jewelry. So a period approach(Victorian, deco, etc.) might work. But I also like a clean, modern look as well. Color scheme will probably revolve around platinum, but again, I'm open to ideas. Thanks!
needs to have business card, letterhead, fax, and envelope design
logo vector file
KX Press business card format
RGB Color Chart
GRA logo

```html
<!DOCTYPE html>
<html lang="en">
<head>
<meta charset="utf-8">
<title>GRA Stationary – Business Card</title>
<link href="https://fonts.googleapis.com/css2?family=Questrial&display=swap" rel="stylesheet">
<style>
  :root {
    --backdrop: #2b2b2d;
    --card-white: #f7f7f7;
    --card-white-edge: #dedede;
    --card-black: #121212;
    --card-black-hi: #2e2e2e;
    --ink: #2a2a2a;
    --ink-soft: #5a5a5a;
    --silver: #b9b9b9;
    --silver-light: #d9d9d9;
    --band: #141414;
  }
  * { margin: 0; padding: 0; box-sizing: border-box; }
  html, body { width: 1200px; height: 901px; overflow: hidden; }
  body {
    background: var(--backdrop);
    font-family: "Questrial", "Century Gothic", sans-serif;
    position: relative;
  }
  .card {
    position: absolute;
    width: 580px;
    height: 331px;
    border-radius: 22px;
    overflow: hidden;
  }
  .card--back {
    left: 70px;
    top: 70px;
    background: linear-gradient(160deg, var(--card-black-hi) 0%, var(--card-black) 55%, #000 100%);
    color: var(--silver);
  }
  .card--back .brand {
    position: absolute;
    left: 0; right: 0; top: 108px;
    text-align: center;
  }
  .card--front {
    left: 550px;
    top: 500px;
    background: linear-gradient(170deg, #ffffff 0%, var(--card-white) 60%, var(--card-white-edge) 100%);
    color: var(--ink);
  }
  .card--front .brand {
    position: absolute;
    left: 0; right: 0; top: 22px;
    text-align: center;
    color: var(--ink);
  }
  .brand__mark {
    display: flex;
    align-items: center;
    justify-content: center;
    gap: 10px;
    font-size: 40px;
    letter-spacing: 4px;
    line-height: 1;
  }
  .brand__dot {
    width: 10px; height: 10px; border-radius: 50%;
    background: currentColor;
  }
  .brand__name {
    margin-top: 10px;
    font-size: 20px;
    letter-spacing: 1px;
  }
  .holder {
    position: absolute;
    left: 58px;
    top: 140px;
    width: 210px;
    text-align: right;
  }
  .holder__name { font-size: 19px; letter-spacing: 0.5px; }
  .holder__title { font-size: 13px; color: var(--ink-soft); margin-top: 4px; }
  .divider {
    position: absolute;
    left: 285px;
    top: 138px;
    width: 1px;
    height: 118px;
    background: var(--silver);
  }
  .contact {
    position: absolute;
    left: 302px;
    top: 138px;
    font-size: 13px;
    line-height: 17px;
    color: var(--ink);
    list-style: none;
  }
  .contact li { display: flex; align-items: center; gap: 7px; white-space: nowrap; }
  .contact svg { width: 11px; height: 11px; fill: var(--ink-soft); flex: none; }
  .band-rule {
    position: absolute;
    left: 0; right: 0;
    height: 3px;
    background: linear-gradient(90deg, var(--silver), var(--silver-light), var(--silver));
  }
  .band-rule--top { top: 270px; }
  .band-rule--bottom { top: 307px; }
  .web-band {
    position: absolute;
    left: 0; right: 0;
    top: 276px;
    height: 28px;
    background: var(--band);
    color: var(--silver-light);
    font-size: 13px;
    letter-spacing: 4px;
    text-align: center;
    line-height: 28px;
  }
</style>
</head>
<body>

<section class="card card--back">
  <div class="brand">
    <div class="brand__mark"><span class="brand__dot"></span>GRA</div>
    <div class="brand__name">Garnet Resale Advisors</div>
  </div>
</section>

<section class="card card--front">
  <div class="brand">
    <div class="brand__mark"><span class="brand__dot"></span>GRA</div>
    <div class="brand__name">Garnet Resale Advisors</div>
  </div>

  <div class="holder">
    <div class="holder__name">Dominic T. Harlow</div>
    <div class="holder__title">President</div>
  </div>

  <div class="divider"></div>

  <ul class="contact">
    <li>P.O. Box 382</li>
    <li>Fernbrook Hill, PA 19507</li>
    <li><svg viewBox="0 0 12 12"><path d="M2 1h2.5l1 3-1.5 1a6 6 0 0 0 3 3l1-1.5 3 1V11c-5 0-9-4-9-9z"/></svg>(888) 555-0182</li>
    <li><svg viewBox="0 0 12 12"><rect x="3" y="0.5" width="6" height="11" rx="1"/></svg>(610) 555-0147</li>
    <li><svg viewBox="0 0 12 12"><rect x="3" y="0.5" width="6" height="4"/><rect x="1" y="4" width="10" height="5" rx="1"/><rect x="3" y="8" width="6" height="3.5"/></svg>(610) 555-0193</li>
    <li><svg viewBox="0 0 12 12"><path d="M0.5 2.5h11v7h-11z M0.5 2.5l5.5 4 5.5-4" fill="none" stroke="#5a5a5a" stroke-width="1.2"/></svg>dtharlow@graadvllc.com</li>
  </ul>

  <div class="band-rule band-rule--top"></div>
  <div class="web-band">www.graadvllc.com</div>
  <div class="band-rule band-rule--bottom"></div>
</section>

</body>
</html>
```